Marigold Rest Pet Cremation, Client catalog

Marigold rest is a Pet crematorium in Melbourne, Aus. This catalogue is to show clients our services , as well as our range of urns, jewellery and keepsake items. Marigold rest provides services for all pets, focusing on exotics, such as rabbits, Guinea pigs, snakes and birds.
- the layout will have pictures with space to add text that will include size and price.
The main colour is N460 After rain with HDC-MD- 08 whisper white, MQ3-27 etched glass and S180-2 sunwashed brick.
Updates

Designs look the same

Target Market(s)

All pet owners

Industry/Entity Type

Funeral, crematorium for Pets

Font styles to use
Script

Colors
0094D4
00A9DD
6FCCEA
C7EBF8
E9F6FB

Requirements
Must have
• Allowing me to upload pictures of items and corresponding price info as needed
Nice to have
• Boho vibes. pastel colour scheme, clean, modern layout.
Should not have
• Paw print symbols and/or love heart symbols. Typical dark, sad vibe. Info overload. It’s a catalog not a brochure

```html
<!DOCTYPE html>
<html lang="en">
<head>
<meta charset="utf-8">
<title>Marigold Rest Pet Cremation – Catalogue</title>
<link href="https://fonts.googleapis.com/css2?family=Damion&family=Roboto:wght@400;500;700;900&display=swap" rel="stylesheet">
<style>
:root{
  --stage:#333333;
  --sky:#dcedf1;
  --sky-light:#e2f2f6;
  --cream:#f4f2ea;
  --blush:#e8c8bb;
  --blush-soft:#f1dcd3;
  --ink:#111111;
  --ink-soft:#3b3b3b;
  --white:#ffffff;
}
*{margin:0;padding:0;box-sizing:border-box}
html,body{width:691px;height:1200px;overflow:hidden}
body{background:var(--stage);font-family:"Roboto",sans-serif;color:var(--ink);position:relative}

/* ---------- Cover ---------- */
.cover{position:absolute;left:35px;top:180px;width:620px;height:401px;background:var(--sky);overflow:hidden}
.cover-photo{position:absolute;inset:0;width:620px;height:401px}
.brand{color:var(--ink);font-family:"Roboto",sans-serif;font-weight:700;line-height:1;white-space:nowrap}
.brand .brand-tag{display:block;text-transform:uppercase;letter-spacing:.42em}
.cover-brand-box{position:absolute;left:472px;top:0;width:134px;height:103px;background:var(--sky-light);display:flex;align-items:center;justify-content:center}
.cover-brand-box .brand{font-size:16px;text-align:center}
.cover-brand-box .brand-tag{font-size:5px;margin-top:5px}
.cover-contact{position:absolute;left:21px;top:259px;width:190px}
.cover-contact .brand{font-size:22px;padding-left:5px;margin-top:16px}
.cover-contact .brand-tag{font-size:6.5px;margin-top:6px;padding-left:14px}
.contact-list{list-style:none;margin-top:14px;padding-left:11px}
.contact-list li{display:flex;align-items:center;gap:9px;height:18px;font-size:8.5px;font-weight:500}
.contact-list li.phone{font-size:10.5px;font-weight:500;letter-spacing:.02em}
.contact-icon{width:15px;height:15px;border-radius:50%;background:var(--blush);display:flex;align-items:center;justify-content:center;flex:none}
.contact-icon svg{width:9px;height:9px}
.cover-title{position:absolute;left:332px;top:270px;width:250px}
.cover-title .script{font-family:"Damion",cursive;line-height:.8;color:var(--ink)}
.cover-title .script-pet{font-size:44px;display:block}
.cover-title .script-main{font-size:46px;display:block;margin-left:14px;margin-top:-6px}
.cover-title .catalogue{display:block;margin-left:18px;margin-top:12px;font-size:16px;font-weight:900;letter-spacing:.3em}

/* ---------- Inner spread ---------- */
.spread{position:absolute;left:35px;top:621px;width:620px;height:401px;background:var(--cream);overflow:hidden}
.spread-header{position:absolute;left:0;top:0;width:620px;height:82px}
.page-brand{position:absolute;top:17px}
.page-brand .brand{font-size:12px}
.page-brand .brand-tag{font-size:3.6px;margin-top:4px;letter-spacing:.5em}
.page-brand.left{left:18px}
.page-brand.right{left:510px}
.service-title{position:absolute;top:18px;font-size:7.4px;font-weight:400;color:var(--ink-soft);white-space:nowrap}
.service-title b{background:var(--blush);color:var(--ink);font-weight:700;padding:0 1px}
.service-title.dog{left:191px}
.service-title.rabbit{left:325px}

.product-photo{position:absolute;width:68px;height:68px;border-radius:50%;border:1.5px solid var(--blush);box-shadow:inset 0 0 0 3px var(--white)}
.ph-urn{background:radial-gradient(circle at 50% 55%,#5b4c49 0 38%,#efe9e4 40%)}
.ph-chain{background:radial-gradient(ellipse at 50% 55%,#f5f1ea 0 12%,#d9a84c 14% 28%,#f7f3ec 31%)}
.ph-plush{background:radial-gradient(circle at 55% 50%,#5a4039 0 34%,#d9d0c8 36% 60%,#b7aba2)}
.ph-box{background:radial-gradient(circle at 45% 55%,#e8d3b5 0 36%,#cbb293 38% 44%,#f6f1ea 46%)}

.product-tag{position:absolute;width:48px;height:48px;border-radius:50%;background:var(--white);border:1px solid var(--blush);display:flex;flex-direction:column;justify-content:center;align-items:stretch;overflow:hidden;text-align:center;font-size:4.4px;line-height:1}
.product-tag span{display:block;padding:1.6px 0}
.product-tag .label{font-weight:700;font-size:5px}
.product-tag .label.price{background:var(--blush-soft)}
.product-tag .value{font-weight:500}
.product-tag .value.first{border-bottom:2px solid var(--blush-soft)}

.page-footer{position:absolute;top:386px;height:8px;display:flex;align-items:center;gap:6px;font-size:3.6px;font-weight:700}
.page-footer .rule{flex:1;height:.6px;background:var(--sky)}
.page-footer .page-no{width:8px;height:8px;border-radius:50%;background:var(--sky);display:flex;align-items:center;justify-content:center;font-size:3.6px}
.page-footer.left{left:13px;width:290px}
.page-footer.right{left:327px;width:285px}
</style>
</head>
<body>

<section class="cover" aria-label="Catalogue cover">
  <svg class="cover-photo" viewBox="0 0 620 401" role="img" aria-label="Photo of a smiling woman in a felt hat cuddling a white dog in warm autumn light">
    <defs>
      <linearGradient id="warmLight" x1="0" y1="0" x2="1" y2="1">
        <stop offset="0" stop-color="#e2a866"/>
        <stop offset=".3" stop-color="#ead2b8"/>
        <stop offset=".55" stop-color="#f3ebe4"/>
        <stop offset=".8" stop-color="#f0dcc6"/>
        <stop offset="1" stop-color="#e8c9a8"/>
      </linearGradient>
      <linearGradient id="fadeToSky" x1="0" y1="0" x2="0" y2="1">
        <stop offset=".45" stop-color="#dcedf1" stop-opacity="0"/>
        <stop offset="1" stop-color="#dcedf1" stop-opacity=".9"/>
      </linearGradient>
    </defs>
    <path d="M0 0H620V401H385C365 335 340 295 305 283C205 258 85 205 0 168Z" fill="url(#warmLight)"/>
    <path d="M0 0H620V401H385C365 335 340 295 305 283C205 258 85 205 0 168Z" fill="url(#fadeToSky)"/>
  </svg>

  <div class="cover-brand-box">
    <p class="brand">Marigold Rest<span class="brand-tag">Pet Cremation</span></p>
  </div>

  <div class="cover-contact">
    <p class="brand">Marigold Rest<span class="brand-tag">Pet Cremation</span></p>
    <ul class="contact-list">
      <li><span class="contact-icon"><svg viewBox="0 0 10 10"><path d="M5 1a3 3 0 0 0-3 3c0 2.2 3 5 3 5s3-2.8 3-5a3 3 0 0 0-3-3z" fill="none" stroke="#111" stroke-width="1"/><circle cx="5" cy="4" r="1" fill="#111"/></svg></span>lorem ipsum address here</li>
      <li class="phone"><span class="contact-icon"><svg viewBox="0 0 10 10"><path d="M2.2 1.5l1.6-.2.8 2-1 .8a5 5 0 0 0 2.3 2.3l.8-1 2 .8-.2 1.6c-3.6.4-6.7-2.7-6.3-6.3z" fill="#111"/></svg></span>0000-000-000</li>
      <li><span class="contact-icon"><svg viewBox="0 0 10 10"><g fill="none" stroke="#111" stroke-width=".8"><circle cx="5" cy="5" r="3.8"/><ellipse cx="5" cy="5" rx="1.6" ry="3.8"/><path d="M1.2 5h7.6M1.8 3h6.4M1.8 7h6.4"/></g></svg></span>Loremipsum.com</li>
    </ul>
  </div>

  <h1 class="cover-title">
    <span class="script script-pet">Pet</span>
    <span class="script script-main">Cremation</span>
    <span class="catalogue">CATALOGUE</span>
  </h1>
</section>

<section class="spread" aria-label="Catalogue pages 1 and 2">
  <svg class="spread-header" viewBox="0 0 620 82" aria-hidden="true">
    <path d="M0 0H620V56C520 58 380 58 310 72C240 58 100 58 0 56Z" fill="#dcedf1"/>
    <path d="M0 58C100 60 240 60 310 74C380 60 520 60 620 58" fill="none" stroke="#e8c8bb" stroke-width="1.6"/>
    <path d="M0 64C100 66 240 66 310 80C380 66 520 66 620 64" fill="none" stroke="#e8c8bb" stroke-width="2"/>
  </svg>

  <div class="page-brand left"><p class="brand">Marigold Rest<span class="brand-tag">Pet Cremation</span></p></div>
  <p class="service-title dog">LOREM IPSUM <b>DOG</b> SERVICE</p>
  <p class="service-title rabbit">LOREM IPSUM <b>RABBITS</b> SERVICE</p>
  <div class="page-brand right"><p class="brand">Marigold Rest<span class="brand-tag">Pet Cremation</span></p></div>

  <!-- Page 1, column 1 -->
  <div class="product-photo ph-urn" style="left:32px;top:74px" role="img" aria-label="Product photo: dark pet urn with name tag"></div>
  <div class="product-tag" style="left:94px;top:102px"><span class="label">SIZE</span><span class="value first">LOREM IPSUM</span><span class="label price">PRICE</span><span class="value">LOREM IPSUM</span></div>
  <div class="product-photo ph-chain" style="left:32px;top:156px" role="img" aria-label="Product photo: gold chain bracelet"></div>
  <div class="product-tag" style="left:94px;top:184px"><span class="label">SIZE</span><span class="value first">LOREM IPSUM</span><span class="label price">PRICE</span><span class="value">LOREM IPSUM</span></div>
  <div class="product-photo ph-plush" style="left:32px;top:231px" role="img" aria-label="Product photo: brown plush keepsake dog"></div>
  <div class="product-tag" style="left:94px;top:259px"><span class="label">SIZE</span><span class="value first">LOREM IPSUM</span><span class="label price">PRICE</span><span class="value">LOREM IPSUM</span></div>
  <div class="product-photo ph-box" style="left:32px;top:305px" role="img" aria-label="Product photo: engraved round wooden keepsake box"></div>
  <div class="product-tag" style="left:94px;top:333px"><span class="label">SIZE</span><span class="value first">LOREM IPSUM</span><span class="label price">PRICE</span><span class="value">LOREM IPSUM</span></div>

  <!-- Page 1, column 2 -->
  <div class="product-photo ph-urn" style="left:211px;top:71px" role="img" aria-label="Product photo: dark pet urn with name tag"></div>
  <div class="product-tag" style="left:173px;top:52px"><span class="label">SIZE</span><span class="value first">LOREM IPSUM</span><span class="label price">PRICE</span><span class="value">LOREM IPSUM</span></div>
  <div class="product-photo ph-chain" style="left:211px;top:145px" role="img" aria-label="Product photo: gold chain bracelet"></div>
  <div class="product-tag" style="left:173px;top:126px"><span class="label">SIZE</span><span class="value first">LOREM IPSUM</span><span class="label price">PRICE</span><span class="value">LOREM IPSUM</span></div>
  <div class="product-photo ph-plush" style="left:211px;top:221px" role="img" aria-label="Product photo: brown plush keepsake dog"></div>
  <div class="product-tag" style="left:173px;top:202px"><span class="label">SIZE</span><span class="value first">LOREM IPSUM</span><span class="label price">PRICE</span><span class="value">LOREM IPSUM</span></div>
  <div class="product-photo ph-box" style="left:211px;top:297px" role="img" aria-label="Product photo: engraved round wooden keepsake box"></div>
  <div class="product-tag" style="left:173px;top:278px"><span class="label">SIZE</span><span class="value first">LOREM IPSUM</span><span class="label price">PRICE</span><span class="value">LOREM IPSUM</span></div>

  <!-- Page 2, column 3 -->
  <div class="product-photo ph-urn" style="left:341px;top:70px" role="img" aria-label="Product photo: dark pet urn with name tag"></div>
  <div class="product-tag" style="left:400px;top:59px"><span class="label">SIZE</span><span class="value first">LOREM IPSUM</span><span class="label price">PRICE</span><span class="value">LOREM IPSUM</span></div>
  <div class="product-photo ph-chain" style="left:341px;top:143px" role="img" aria-label="Product photo: gold chain bracelet"></div>
  <div class="product-tag" style="left:400px;top:132px"><span class="label">SIZE</span><span class="value first">LOREM IPSUM</span><span class="label price">PRICE</span><span class="value">LOREM IPSUM</span></div>
  <div class="product-photo ph-plush" style="left:341px;top:213px" role="img" aria-label="Product photo: brown plush keepsake dog"></div>
  <div class="product-tag" style="left:400px;top:202px"><span class="label">SIZE</span><span class="value first">LOREM IPSUM</span><span class="label price">PRICE</span><span class="value">LOREM IPSUM</span></div>
  <div class="product-photo ph-box" style="left:341px;top:288px" role="img" aria-label="Product photo: engraved round wooden keepsake box"></div>
  <div class="product-tag" style="left:400px;top:277px"><span class="label">SIZE</span><span class="value first">LOREM IPSUM</span><span class="label price">PRICE</span><span class="value">LOREM IPSUM</span></div>

  <!-- Page 2, column 4 -->
  <div class="product-photo ph-urn" style="left:521px;top:85px" role="img" aria-label="Product photo: dark pet urn with name tag"></div>
  <div class="product-tag" style="left:483px;top:110px"><span class="label">SIZE</span><span class="value first">LOREM IPSUM</span><span class="label price">PRICE</span><span class="value">LOREM IPSUM</span></div>
  <div class="product-photo ph-chain" style="left:521px;top:158px" role="img" aria-label="Product photo: gold chain bracelet"></div>
  <div class="product-tag" style="left:483px;top:183px"><span class="label">SIZE</span><span class="value first">LOREM IPSUM</span><span class="label price">PRICE</span><span class="value">LOREM IPSUM</span></div>
  <div class="product-photo ph-plush" style="left:521px;top:234px" role="img" aria-label="Product photo: brown plush keepsake dog"></div>
  <div class="product-tag" style="left:483px;top:259px"><span class="label">SIZE</span><span class="value first">LOREM IPSUM</span><span class="label price">PRICE</span><span class="value">LOREM IPSUM</span></div>
  <div class="product-photo ph-box" style="left:521px;top:308px" role="img" aria-label="Product photo: engraved round wooden keepsake box"></div>
  <div class="product-tag" style="left:483px;top:333px"><span class="label">SIZE</span><span class="value first">LOREM IPSUM</span><span class="label price">PRICE</span><span class="value">LOREM IPSUM</span></div>

  <footer class="page-footer left"><span>Loremipsum.com</span><span class="rule"></span><span class="page-no">01</span></footer>
  <footer class="page-footer right"><span>Loremipsum.com</span><span class="rule"></span><span class="page-no">02</span></footer>
</section>

</body>
</html>
```